Flyer Design Project for lawn care business

I need a flyer designed for my lawn care business, "Hadley's Groundskeeping Services".  It is a family owned small landscaping company. I was thinking something that I can print  2- 3 per page.
I have  2 different logos I can upload to give an idea.  I have seen some I like that are colorfull with neat graphics but I also like some that are simple and elegant.  I would like something that catches your eye and looks professionaly done.

Target Market(s)
Homeowners in Durham, North Carolina with homes usually valued $200,000 or more.
Industry/Entity Type
Landscaping
Requirements
Must have
- I would like the address of my website listed on it, www.hadleygroundskeepingservices.example
I would like for it to say somewhere, 50% off first service with seasonal service.
Not sure if I want to list some of the services that I offer or just say full service lawn care.
Nice to have
- I have a logo with a bull pushing a lawn mower.  I live in Durham, NC also known as the Bull City.  I am not in love with the logo so feel free to change it or not use it at all.

```html
<!DOCTYPE html>
<html lang="en">
<head>
<meta charset="utf-8">
<title>Hadley's Lawn Care &amp; Maintenance Service Flyer</title>
<link rel="stylesheet" href="https://fonts.googleapis.com/css2?family=Alfa+Slab+One&family=Roboto+Condensed:wght@700&family=Oswald:wght@500&display=swap">
<style>
  :root {
    --bg-light: #fbf6ea;
    --bg-mid: #ece2d0;
    --bg-edge: #d9cdb8;
    --brand-green: #5cb048;
    --deep-green: #2f7d3a;
    --badge-green: #2e9a48;
    --brick-red: #8a1b12;
    --text-brown: #564840;
    --text-dark: #4a4140;
    --panel: rgba(196, 192, 150, 0.55);
    --chip: #cbc4a6;
    --white: #ffffff;
  }
  html, body { margin: 0; padding: 0; overflow: hidden; }
  body { width: 1200px; height: 800px; }
  .flyer {
    position: relative;
    width: 1200px;
    height: 800px;
    overflow: hidden;
    background: radial-gradient(ellipse at 45% 35%, var(--bg-light) 0%, var(--bg-mid) 65%, var(--bg-edge) 100%);
    font-family: "Roboto Condensed", "Arial Narrow", sans-serif;
  }
  .brand-mark {
    position: absolute;
    left: 58px; top: 100px;
    display: flex; align-items: center; gap: 14px;
    font-weight: 700; font-size: 62px; color: var(--brick-red);
  }
  .brand-mark .dot {
    width: 34px; height: 34px; border-radius: 50%; background: var(--brick-red);
  }
  .headline {
    position: absolute; margin: 0;
    font-family: "Alfa Slab One", Georgia, serif; font-weight: 400;
    color: var(--brand-green); font-size: 58px; line-height: 1; white-space: nowrap;
  }
  .headline.line-1 { left: 400px; top: 46px; }
  .headline.line-2 { left: 440px; top: 106px; }
  .headline .amp { font-size: 34px; }
  .website {
    position: absolute; left: 505px; top: 160px;
    font-weight: 700; font-size: 22px; color: var(--deep-green); letter-spacing: 0.5px;
  }
  .tagline {
    position: absolute; left: 395px; top: 228px;
    font-weight: 700; font-size: 34px; color: var(--text-brown); word-spacing: 4px;
  }
  .services-title {
    position: absolute; left: 0; width: 1200px; top: 330px; text-align: center;
    margin: 0; padding-right: 0;
    font-family: "Alfa Slab One", Georgia, serif; font-weight: 400;
    font-size: 38px; letter-spacing: 17px; color: var(--brand-green);
    text-indent: -2px;
  }
  .services-panel {
    position: absolute; left: 132px; top: 386px; width: 908px; height: 118px;
    background: var(--panel); border-radius: 6px;
    display: flex; align-items: center; margin: 0; padding: 0; list-style: none;
  }
  .services-panel li {
    font-family: "Alfa Slab One", Georgia, serif; font-size: 38px; color: var(--brick-red);
    padding: 0 22px 0 10px; height: 78px; display: flex; align-items: center;
    border-right: 2px solid rgba(138, 27, 18, 0.55);
  }
  .services-panel li:first-child { padding-left: 12px; }
  .services-panel li:last-child { border-right: none; }
  .consult {
    position: absolute; left: 140px; top: 510px;
    font-weight: 700; font-size: 30px; color: var(--text-dark);
  }
  .phone {
    position: absolute; left: 140px; top: 556px;
    font-weight: 700; font-size: 26px; color: var(--text-dark); letter-spacing: 0.5px;
  }
  .specials {
    position: absolute; left: 360px; top: 585px; width: 466px; height: 58px;
    background: var(--chip); border-radius: 4px;
    display: flex; align-items: center; justify-content: center;
    font-weight: 700; font-size: 28px; color: var(--text-dark);
  }
  .service-area {
    position: absolute; left: 240px; width: 700px; top: 656px; text-align: center;
    font-weight: 700; font-size: 26px; line-height: 36px; color: var(--brick-red); margin: 0;
  }
  .lawn-strip {
    position: absolute; left: 0; bottom: 0; width: 1200px; height: 130px;
    background: linear-gradient(to bottom, rgba(120, 190, 60, 0) 0%, #8bcb3f 35%, #4f9a22 100%);
  }
  .offer-badge { position: absolute; left: 915px; top: 425px; width: 300px; height: 300px; }
  .offer-badge text {
    font-family: "Oswald", "Arial Narrow", sans-serif; font-weight: 500;
    fill: var(--white); font-size: 25px; text-anchor: middle;
  }
</style>
</head>
<body>
<main class="flyer">
  <div class="brand-mark"><span class="dot"></span>Hadley's</div>

  <h1 class="headline line-1">Hadley's Lawn Care</h1>
  <h1 class="headline line-2"><span class="amp">&amp;</span>Maintenance Service</h1>
  <div class="website">www.hadleygroundskeepingservices.example</div>

  <div class="tagline">Not Just Lawn Care.&nbsp; We Do Complete Home Repair.</div>

  <h2 class="services-title">SERVICES OFFERED</h2>
  <ul class="services-panel">
    <li>Landscaping</li>
    <li>Carpentry</li>
    <li>Plumbing</li>
    <li>Hvac</li>
  </ul>

  <div class="consult">Schedule A Free Home Consultation &amp; Quote</div>
  <div class="phone">(919) 555-0142</div>
  <div class="specials">We Offer Specials &amp; Discounts</div>

  <div class="lawn-strip" role="img" aria-label="Strip of green grass along the bottom edge"></div>

  <p class="service-area">Providing Lawn Care, &amp; Complete Home<br>Repair To Durham, Raleigh &amp; The Rest Of The Triangle</p>

  <svg class="offer-badge" viewBox="0 0 300 300" aria-label="50% off 1st service with seasonal service">
    <g fill="var(--badge-green)">
      <rect x="51" y="51" width="198" height="198"/>
      <rect x="51" y="51" width="198" height="198" transform="rotate(22.5 150 150)"/>
      <rect x="51" y="51" width="198" height="198" transform="rotate(45 150 150)"/>
      <rect x="51" y="51" width="198" height="198" transform="rotate(67.5 150 150)"/>
    </g>
    <g transform="rotate(58 150 150)">
      <text x="150" y="102">50% OFF 1ST</text>
      <text x="150" y="134">SERVICE WITH</text>
      <text x="150" y="166">SEASONAL</text>
      <text x="150" y="198">SERVICE</text>
    </g>
  </svg>
</main>
</body>
</html>
```